New eyelid plastic surgery office needs a business card design-Eyelid Specialists of the Brenwick

I recently used DraftHarbor for my logo design and was very pleased with creativity and results. It was a difficult decision for me. Now I would like to create a business card based on this logo, which I will attach.

The text should be easily legible as some of my patients have difficulty seeing, but I would like a subtle, sophisticated artistry also evident to make the card memorable. Would like the card based on a similar color scheme as the logo but the inverse or other complementary colors may prove interesting

A good question was asked...my concern about my visually impaired patients was really my desire to avoid italicized or calligraphic type fonts that may be hard to read. Standard font size for a business card would be fine. Thanks!

Thank you so much for the great work so far. I wanted to give you my particular contact information to see if that would change the look of the cards. Martin Holloway, MD Address: 2871 Larkspur Lane, Suite 215 Harrowgate, NC 39512 Phone: 555-382-1946 Fax: 555-382-1947 Website: www.brenwickliddesign.example Please delete the email slot from the card. Thanks so much!

Reason: Last minute consideration. So many great revisions right now!

Plastic

```html
<!DOCTYPE html>
<html lang="en">
<head>
<meta charset="utf-8">
<title>Eyelid Specialists of the Brenwick – Business Card</title>
<link rel="stylesheet" href="https://fonts.googleapis.com/css2?family=Arimo:wght@400;700&family=Tinos:wght@400;700&display=swap">
<style>
  :root {
    --stage: #1c1a2e;
    --card-white: #ffffff;
    --aqua-soft: #c9f7fb;
    --aqua: #7fe7f0;
    --aqua-pattern: #a6eff5;
    --navy: #1d3f8f;
    --ink: #111111;
  }
  * { margin: 0; padding: 0; box-sizing: border-box; }
  html, body {
    width: 1200px; height: 888px; overflow: hidden;
    background: var(--stage);
  }
  .business-card {
    position: absolute; left: 100px; top: 158px;
    width: 1000px; height: 572px;
    background: linear-gradient(180deg, var(--card-white) 0%, var(--card-white) 30%, var(--aqua-soft) 60%, var(--aqua) 100%);
    overflow: hidden;
    box-shadow: 0 10px 30px rgba(0,0,0,.45);
  }
  .pattern-band {
    position: absolute; left: 0; right: 0; bottom: 0; height: 62%;
    background: linear-gradient(180deg, rgba(166,239,245,0) 0%, var(--aqua-pattern) 60%, var(--aqua) 100%);
    opacity: .7;
  }
  .practice-name {
    position: absolute; left: 150px; right: 60px; top: 78px;
    font-family: "Tinos", serif; font-weight: 400;
    color: var(--navy); font-size: 66px; line-height: 1.05;
    letter-spacing: 1px; text-align: center;
  }
  .tagline {
    position: absolute; left: 0; right: 0; top: 262px;
    font-family: "Tinos", serif; font-weight: 700;
    color: var(--ink); font-size: 36px; text-align: center;
  }
  .doctor-name {
    position: absolute; left: 210px; top: 350px;
    font-family: "Arimo", sans-serif; font-weight: 700;
    color: var(--ink); font-size: 30px;
  }
  .contact-label-lead {
    position: absolute; left: 90px; top: 362px;
    font-family: "Arimo", sans-serif; font-weight: 700; font-size: 19px; color: var(--ink);
  }
  .contact-list {
    position: absolute; left: 90px; top: 404px;
    font-family: "Arimo", sans-serif; font-weight: 700; font-size: 19px; color: var(--ink);
    display: grid; grid-template-columns: 96px auto; row-gap: 4px;
  }
</style>
</head>
<body>
  <div class="business-card">
    <div class="pattern-band" role="img" aria-label="Soft aqua ornamental lace pattern across the lower half of the card"></div>
    <div class="practice-name">Eyelid Specialists of the Brenwick</div>
    <div class="tagline">New eyelid plastic surgery office</div>
    <div class="contact-label-lead">Contact&nbsp;&nbsp;:</div>
    <div class="doctor-name">Martin Holloway, MD</div>
    <div class="contact-list">
      <span>Address</span><span>: 2871 Larkspur Lane, Suite 215 Harrowgate, NC 39512</span>
      <span>Phone</span><span>: 555 - 382 - 1946</span>
      <span>Fax</span><span>: 555 - 382 - 1947</span>
      <span>web</span><span>: www.brenwickliddesign.example</span>
    </div>
  </div>
</body>
</html>
```